Vask - Website Design in WordPress (2 pages)

The goal of this design work is to create two highly focused, PPC- and SEO-aware landing pages that clearly explain the experience in familiar terms and drive app installs. The design must respect the existing visual identity and support future iteration of copy and content without requiring redesign.
Required Deliverables:
Fully working WordPress site containing:
Homepage template
Location landing page template
Mobile-first, responsive
CTA behaviour exactly as designed
Required
WordPress admin access
Full site export / backup
Homepage template
Mobile-first behaviour
CTA visible above the fold on mobile
Uses my:
Visual identity
Logo
Placeholder copy
I receive:
Admin access
Full site export / backup
Not acceptable
20+ plugins
Proprietary or abandoned builders
Hardcoded layouts that can’t be reused
Separate page designs per location
Elementor is preferred if:
One builder only
Clean structure
No custom lock-in widgets
Uploaded the mobile design for inspiration only

```html
<!DOCTYPE html>
<html lang="en">
<head>
<meta charset="utf-8">
<title>Vask — Location puzzle games</title>
<link href="https://fonts.googleapis.com/css2?family=Outfit:wght@400;500;600;700&family=Nunito+Sans:wght@400;600;700;800&display=swap" rel="stylesheet">
<style>
:root{
  --teal:#167f8c;
  --teal-dark:#116a76;
  --teal-light:#4cc4c8;
  --orange:#f15f26;
  --orange-soft:#f58a5a;
  --cream:#fdf3ea;
  --peach:#fde4d6;
  --ink:#1f2a30;
  --muted:#5e6a70;
  --white:#ffffff;
  --screen:#f3f6f6;
}
*{box-sizing:border-box;margin:0;padding:0}
html,body{width:1200px;height:3995px;overflow:hidden}
body{font-family:"Nunito Sans",sans-serif;color:var(--ink);background:linear-gradient(180deg,#e7f1ee 0,#fbeee4 12%,var(--cream) 40%,#fbf1e8 100%);position:relative}
.abs{position:absolute}
h1,h2,h3,.display{font-family:"Outfit",sans-serif}
.logo{font-family:"Outfit",sans-serif;font-weight:700;color:var(--teal);letter-spacing:-1px;line-height:1}

/* store buttons */
.stores{display:flex;gap:12px}
.store{display:flex;align-items:center;gap:7px;background:#fff;border:1.5px solid #2b2b2b;border-radius:6px;height:38px;padding:0 10px;color:#111;font-family:"Nunito Sans",sans-serif}
.store.dark{background:#fff}
.store .ic{width:18px;height:18px;border-radius:4px;background:var(--teal)}
.store.alt .ic{background:var(--ink);border-radius:50%}
.store small{display:block;font-size:7px;font-weight:700;line-height:1;text-transform:uppercase}
.store b{display:block;font-size:15px;font-weight:700;line-height:1.05}

/* phone */
.phone{position:absolute;background:#111;border-radius:34px;padding:9px;box-shadow:0 18px 40px rgba(0,0,0,.18)}
.phone .screen{position:relative;width:100%;height:100%;border-radius:26px;overflow:hidden;background:var(--screen)}
.notch{position:absolute;top:9px;left:50%;transform:translateX(-50%);width:60px;height:6px;border-radius:4px;background:#111;z-index:3}
.status{position:absolute;top:12px;left:24px;right:22px;display:flex;justify-content:space-between;font-size:9px;font-weight:700;z-index:3}
.plate{width:100%;border-radius:8px}

/* login screen */
.login{background:linear-gradient(180deg,#24343a 0,#1d2b30 60%,#162226 100%);color:#fff}
.login .hero-shot{position:absolute;inset:0 0 45% 0;background:linear-gradient(180deg,#3a4b50,#23333a 70%,#1d2b30)}
.login .content{position:absolute;left:22px;right:22px;top:0}
.field{height:26px;border-radius:5px;background:#fff;color:#888;font-size:10px;display:flex;align-items:center;padding-left:28px}
.btn-teal{height:28px;border-radius:14px;background:var(--teal);color:#fff;font-size:10px;font-weight:700;display:flex;align-items:center;justify-content:center}
.social{display:flex;justify-content:center;gap:16px}
.social span{width:26px;height:26px;border-radius:50%;border:1.5px solid #fff}

/* dashboard screen */
.dash .top{position:absolute;left:0;right:0;top:0;height:150px;background:var(--teal);border-radius:0 0 18px 18px;color:#fff}
.avatar{width:30px;height:30px;border-radius:50%;background:#e8d6c6;border:2px solid #fff}
.card{background:#e6f1f1;border-radius:10px;text-align:center;color:var(--muted)}
.thumb{border-radius:6px;background:linear-gradient(135deg,#7a5a3a,#c79a64 50%,#5a3e28)}
.thumb.night{background:linear-gradient(135deg,#1b2c3a,#3a5566 50%,#8a4a2a)}

/* games screen */
.games .top{position:absolute;left:0;right:0;top:0;height:112px;background:var(--teal);color:#fff}
.tabs{display:flex;background:var(--teal-dark);border-radius:14px;padding:3px;gap:2px}
.tabs span{flex:1;text-align:center;font-size:10px;padding:5px 0;border-radius:11px}
.tabs span.on{background:#3d9ba6}
.chips{display:flex;gap:6px}
.chips span{background:#e2e8e8;border-radius:12px;font-size:9px;padding:5px 9px;color:#333;white-space:nowrap}
.gcard{background:#fff;border-radius:8px;box-shadow:0 2px 8px rgba(0,0,0,.08);padding:6px}
.stars{color:var(--orange);font-size:10px;letter-spacing:1px}
.tag{display:inline-block;font-size:8px;color:#fff;border-radius:3px;padding:1px 5px}

/* benefits */
.benefit{position:absolute;width:290px;display:flex;gap:14px}
.benefit .b-ic{flex:none;width:60px;height:60px;border-radius:50%;background:#fff;box-shadow:0 4px 14px rgba(0,0,0,.07);display:flex;align-items:center;justify-content:center}
.benefit h3{font-size:17px;font-weight:500;margin:8px 0 12px}
.benefit p{font-size:10.5px;line-height:1.3;color:#333}

/* steps */
.step{position:absolute;width:180px;text-align:center;top:1405px}
.step .num{width:38px;height:38px;border-radius:50%;background:var(--teal-light);color:#fff;font-family:"Outfit",sans-serif;font-size:18px;display:flex;align-items:center;justify-content:center;margin:0 auto 18px}
.step h3{font-size:17px;font-weight:500;margin-bottom:8px}
.step p{font-size:10px;line-height:1.3;color:#333}

/* stats */
.stat{position:absolute;display:flex;flex-direction:column;align-items:center;justify-content:center;text-align:center;font-family:"Outfit",sans-serif;line-height:1}
.stat b{font-weight:600}
.stat small{font-size:11px;font-weight:500;margin-top:4px}

.partner{position:absolute;top:2710px;width:182px;height:75px;background:#fff;display:flex;align-items:center;justify-content:center}
.partner span{display:block;border-radius:6px}

.foot-link{font-size:12px;color:#222}
.foot-social{width:28px;height:28px;border-radius:50%;background:var(--teal);display:inline-block}
</style>
</head>
<body>

<!-- ============ HERO ============ -->
<svg class="abs" style="left:0;top:0" width="1200" height="800" aria-hidden="true">
  <path d="M740 0 H1200 V760 Q1150 790 1080 720 L1000 640 Q960 600 880 610 L760 620 Q640 620 620 480 L615 320 Q610 210 690 120 Z" fill="var(--orange)"/>
  <circle cx="1150" cy="40" r="60" fill="var(--orange-soft)" opacity=".6"/>
  <circle cx="707" cy="136" r="31" fill="var(--teal-light)"/>
</svg>

<div class="logo abs" style="left:104px;top:8px;font-size:62px">vask</div>

<p class="abs" style="left:105px;top:244px;font-family:Outfit,sans-serif;font-size:19px;color:var(--teal);font-weight:500">We've just released a brand-new location puzzle:</p>
<h1 class="abs" style="left:105px;top:276px;font-size:46px;line-height:1.28;color:var(--orange);font-weight:500">The Echoes of Riverside<br>Park.</h1>
<p class="abs" style="left:105px;top:412px;font-size:14px">Grab your team and start the challenge now!</p>
<div class="stores abs" style="left:105px;top:461px">
  <div class="store"><span class="ic"></span><div><small>Get it on</small><b>PlayHub</b></div></div>
  <div class="store alt"><span class="ic"></span><div><small>Download on the</small><b>AppVault</b></div></div>
</div>

<div class="phone" style="left:823px;top:138px;width:270px;height:525px">
  <div class="screen login">
    <div class="hero-shot" role="img" aria-label="Team of players standing in a city at dusk"></div>
    <div class="notch"></div>
    <div class="status"><span>9:41</span><span>●●●</span></div>
    <div class="content">
      <div class="logo" style="color:#fff;font-size:50px;margin-top:42px;text-align:center">vask</div>
      <p style="font-size:14px;margin-top:78px">WELCOME BACK!</p>
      <p style="font-size:10px;margin-top:2px">Sign in to continue!</p>
      <div class="field" style="margin-top:12px">Email</div>
      <div class="field" style="margin-top:20px">Password</div>
      <p style="font-size:10px;color:var(--teal-light);text-align:right;margin-top:14px">Forgot password?</p>
      <div class="btn-teal" style="margin-top:16px">LOGIN</div>
      <p style="font-size:10px;text-align:center;margin-top:16px;color:#ccc">Or sign in with</p>
      <div class="social" style="margin-top:10px"><span></span><span></span><span></span></div>
      <p style="font-size:10px;text-align:center;margin-top:18px">Don't have an account? <span style="color:var(--teal-light)">Sign Up</span></p>
    </div>
  </div>
</div>

<!-- ============ BENEFITS ============ -->
<svg class="abs" style="left:0;top:680px" width="440" height="560" aria-hidden="true">
  <path d="M0 60 Q120 -20 260 20 Q400 70 420 220 Q430 380 330 470 L0 470 Z" fill="var(--teal-light)"/>
  <circle cx="20" cy="200" r="44" fill="#6fd1d3" opacity=".6"/>
  <circle cx="54" cy="524" r="31" fill="var(--orange)"/>
</svg>

<div class="phone" style="left:107px;top:725px;width:270px;height:512px">
  <div class="screen dash">
    <div class="top">
      <div class="status" style="color:#fff"><span>9:41</span><span>●●●</span></div>
      <div class="logo" style="color:#fff;font-size:36px;position:absolute;left:16px;top:38px">vask</div>
      <span style="position:absolute;right:16px;top:44px;width:26px;height:26px;border-radius:50%;background:var(--teal-light)"></span>
      <div style="position:absolute;left:16px;top:88px;display:flex;gap:8px;align-items:center">
        <span class="avatar" role="img" aria-label="Player avatar"></span>
        <div><p style="font-size:12px;font-weight:700">Tomas Lindqvist</p><p style="font-size:8px">The Lightseekers Team</p></div>
      </div>
      <div style="position:absolute;left:24px;top:128px;font-size:12px;display:flex;gap:22px;line-height:1">
        <div>72<br><span style="font-size:7px">Level</span></div><div>24<br><span style="font-size:7px">Mission</span></div>
      </div>
      <div style="position:absolute;left:150px;top:132px;width:88px;height:4px;background:#5fb9c1;border-radius:2px"><div style="width:74%;height:4px;background:#9fe0e3;border-radius:2px"></div></div>
    </div>
    <div class="card" style="position:absolute;left:14px;right:14px;top:175px;padding:14px 10px 12px">
      <p style="font-size:12px;font-weight:700;color:#333">ANNOUNCEMENT</p>
      <p style="font-size:9.5px;line-height:1.35;margin-top:10px">We've just released a brand-new location puzzle: "The Echoes of Riverside Park." Grab your team and start the challenge now!</p>
    </div>
    <p style="position:absolute;left:14px;top:335px;font-size:12px;font-weight:700;color:#333">FEATURED NEARBY GAMES</p>
    <div class="thumb" style="position:absolute;left:20px;top:360px;width:128px;height:95px" role="img" aria-label="Old map on a wooden desk"></div>
    <div class="thumb night" style="position:absolute;left:178px;top:360px;width:80px;height:95px" role="img" aria-label="City street at night"></div>
    <p style="position:absolute;left:20px;top:482px;font-size:10px;font-weight:700">The Hidden Archives</p>
  </div>
</div>

<p class="abs" style="left:518px;top:768px;font-family:Outfit,sans-serif;font-size:19px;color:var(--teal);font-weight:500">Our Value</p>
<h2 class="abs" style="left:518px;top:798px;font-size:46px;color:var(--orange);font-weight:500">Vask benefits</h2>

<div class="benefit" style="left:512px;top:890px"><span class="b-ic"><svg width="28" height="28" viewBox="0 0 24 24" fill="none" stroke="var(--orange)" stroke-width="1.6"><path d="M12 21s-6-5.6-6-11a6 6 0 0 1 12 0c0 5.4-6 11-6 11z"/><circle cx="12" cy="10" r="2.3" stroke="var(--teal)"/></svg></span><div><h3>Everywhere access</h3><p>There are many variations of passages of lorem ipsum available.</p></div></div>
<div class="benefit" style="left:830px;top:890px"><span class="b-ic"><svg width="28" height="28" viewBox="0 0 24 24" fill="none" stroke="var(--orange)" stroke-width="1.6"><path d="M12 3l7 3v6c0 4.5-3 7.5-7 9-4-1.5-7-4.5-7-9V6z"/><circle cx="12" cy="12" r="3" stroke="var(--teal)"/></svg></span><div><h3>High security</h3><p>There are many variations of passages of lorem ipsum available.</p></div></div>
<div class="benefit" style="left:512px;top:983px"><span class="b-ic"><svg width="30" height="28" viewBox="0 0 26 24" fill="none" stroke="var(--orange)" stroke-width="1.6"><rect x="2" y="4" width="15" height="11" rx="1"/><rect x="15" y="9" width="8" height="12" rx="1.5" stroke="var(--teal)"/><path d="M6 19h7"/></svg></span><div><h3>All devices synchronized</h3><p>There are many variations of passages of lorem ipsum available.</p></div></div>
<div class="benefit" style="left:830px;top:983px"><span class="b-ic"><svg width="28" height="28" viewBox="0 0 24 24" fill="none" stroke="var(--orange)" stroke-width="1.6"><rect x="6" y="2" width="12" height="20" rx="2"/><path d="M12 7v7m-3-3l3 3 3-3" stroke="var(--teal)"/></svg></span><div><h3>Free download</h3><p>There are many variations of passages of lorem ipsum available.</p></div></div>

<div class="stores abs" style="left:512px;top:1080px">
  <div class="store"><span class="ic"></span><div><small>Get it on</small><b>PlayHub</b></div></div>
  <div class="store alt"><span class="ic"></span><div><small>Download on the</small><b>AppVault</b></div></div>
</div>

<!-- ============ HOW IT WORKS ============ -->
<h2 class="abs" style="left:0;width:1200px;text-align:center;top:1312px;font-size:46px;color:var(--orange);font-weight:500">How it works</h2>
<svg class="abs" style="left:0;top:1400px" width="1200" height="40" aria-hidden="true" fill="none" stroke="#333" stroke-width="1" stroke-dasharray="3 3">
  <path d="M342 20 Q390 5 440 18"/><path d="M548 20 Q596 5 646 18"/><path d="M754 20 Q802 5 852 18"/>
</svg>
<div class="step" style="left:199px"><div class="num">1</div><h3>Install Vask app</h3><p>There are many variations of passages of lorem ipsum available.</p></div>
<div class="step" style="left:405px"><div class="num">2</div><h3>Create account</h3><p>There are many variations of passages of lorem ipsum available.</p></div>
<div class="step" style="left:611px"><div class="num">3</div><h3>Team setup</h3><p>There are many variations of passages of lorem ipsum available.</p></div>
<div class="step" style="left:818px"><div class="num">4</div><h3>Enjoy the game</h3><p>There are many variations of passages of lorem ipsum available.</p></div>
<div class="stores abs" style="left:475px;top:1538px">
  <div class="store"><span class="ic"></span><div><small>Get it on</small><b>PlayHub</b></div></div>
  <div class="store alt"><span class="ic"></span><div><small>Download on the</small><b>AppVault</b></div></div>
</div>

<!-- ============ DIFFERENT ============ -->
<svg class="abs" style="left:0;top:1640px" width="1200" height="850" aria-hidden="true">
  <path d="M0 80 Q180 20 380 70 Q560 120 760 50 Q980 -20 1200 60 V780 Q1000 700 800 760 Q600 820 400 770 Q200 720 0 800 Z" fill="var(--teal)"/>
  <path d="M1200 110 L1200 450 Q1050 420 960 360 L880 300 Q840 270 900 230 Z" fill="var(--orange)"/>
  <circle cx="695" cy="230" r="80" fill="var(--orange)"/>
  <path d="M760 500 L960 470 Q995 465 992 500 L985 700 Q980 735 945 740 L760 760 Q735 762 738 735 L745 520 Q746 502 760 500 Z" fill="var(--teal-light)"/>
</svg>

<h2 class="abs" style="left:200px;top:1832px;font-size:46px;line-height:1.3;color:#fff;font-weight:500">What makes it<br>different</h2>
<div class="stat" style="left:200px;top:1993px;width:112px;height:112px;background:var(--teal-light);color:#fff;border-radius:56px 56px 56px 0"><b style="font-size:42px">5k</b><small>Active users</small></div>
<div class="stat" style="left:358px;top:1982px;width:96px;height:96px;background:#fff;color:#111;border-radius:48px 0 48px 48px"><b style="font-size:28px">10k</b><small style="font-size:10px">Downloads</small></div>
<div class="stat" style="left:200px;top:2155px;width:78px;height:78px;background:var(--peach);color:#111;border-radius:39px 39px 0 39px"><b style="font-size:22px">12k</b><small style="font-size:9px">Reviews</small></div>
<div class="stat" style="left:355px;top:2120px;width:100px;height:100px;background:var(--peach);color:#111;border-radius:50px 50px 50px 0"><b style="font-size:26px">09</b><small style="font-size:10px">Lorem ipsum</small></div>
<p class="abs" style="left:200px;top:2264px;width:380px;font-size:12px;line-height:1.5;color:#fff">Lorem ipsum is simply dummy text of the printing and typesetting industry. lorem ipsum has been the industry.</p>
<div class="stores abs" style="left:200px;top:2333px">
  <div class="store"><span class="ic"></span><div><small>Get it on</small><b>PlayHub</b></div></div>
  <div class="store alt"><span class="ic"></span><div><small>Download on the</small><b>AppVault</b></div></div>
</div>

<div class="phone" style="left:673px;top:1820px;width:270px;height:512px">
  <div class="screen games">
    <div class="top">
      <div class="status" style="color:#fff"><span>9:41</span><span>●●●</span></div>
      <p style="position:absolute;left:16px;top:48px;font-family:Outfit,sans-serif;font-size:20px;font-weight:500">Games</p>
      <span style="position:absolute;right:46px;top:48px;width:24px;height:24px;border-radius:50%;background:var(--teal-light)"></span>
      <span style="position:absolute;right:16px;top:48px;width:24px;height:24px;border-radius:50%;background:var(--teal-light)"></span>
      <div class="tabs" style="position:absolute;left:12px;right:12px;top:80px"><span class="on">Available</span><span>Purchased</span><span>Completed</span></div>
    </div>
    <div class="chips" style="position:absolute;left:12px;top:128px"><span>clue-hunting</span><span>puzzle</span><span>mystery</span><span>exploration</span></div>
    <p style="position:absolute;left:12px;top:180px;font-size:12px;font-weight:700;color:#333">RECOMMENDED GAME</p>
    <div class="gcard" style="position:absolute;left:12px;top:200px;width:140px">
      <div class="thumb" style="height:95px" role="img" aria-label="Old map on a wooden desk"></div>
      <p style="font-size:10.5px;font-weight:700;margin-top:5px">The Hidden Archives</p>
      <p class="stars">★★★★☆</p>
      <div style="display:flex;justify-content:space-between;align-items:center;margin-top:2px"><span class="tag" style="background:#e25a5a">Hard</span><span style="font-size:11px;font-weight:700">$ 48</span></div>
    </div>
    <div class="gcard" style="position:absolute;left:162px;top:200px;width:140px">
      <div class="thumb night" style="height:95px" role="img" aria-label="Team of players in a city"></div>
      <p style="font-size:10.5px;font-weight:700;margin-top:5px">Metro Cipher</p>
      <p class="stars">★★★★☆</p>
      <span class="tag" style="background:#f39a2b">Medium</span>
    </div>
    <p style="position:absolute;right:12px;top:395px;font-size:10px;color:var(--teal)">View All</p>
    <p style="position:absolute;left:12px;top:428px;font-size:12px;font-weight:700;color:#333">TOP GAMES</p>
    <p style="position:absolute;left:120px;top:490px;font-size:10px;font-weight:700">Metro Cipher Hunt</p>
  </div>
</div>

<!-- ============ TRUSTED ============ -->
<h2 class="abs" style="left:0;width:1200px;text-align:center;top:2618px;font-size:46px;color:var(--orange);font-weight:500">Trusted by</h2>
<div class="partner" style="left:200px" role="img" aria-label="Partner badge"><span style="width:120px;height:24px;background:#cfe3c8"></span></div>
<div class="partner" style="left:406px" role="img" aria-label="Partner badge"><span style="width:130px;height:24px;background:#d8d8dc"></span></div>
<div class="partner" style="left:612px" role="img" aria-label="Partner badge"><span style="width:100px;height:44px;background:#2a5aa0"></span></div>
<div class="partner" style="left:818px" role="img" aria-label="Partner badge"><span style="width:120px;height:24px;background:#d4d9cf"></span></div>
<div class="abs" style="left:578px;top:2815px;display:flex;gap:6px">
  <span style="width:6px;height:6px;border-radius:50%;background:#b8d8dc"></span><span style="width:6px;height:6px;border-radius:50%;background:var(--orange)"></span><span style="width:6px;height:6px;border-radius:50%;background:#b8d8dc"></span><span style="width:6px;height:6px;border-radius:50%;background:#b8d8dc"></span>
</div>

<!-- ============ JOIN ============ -->
<svg class="abs" style="left:0;top:2880px" width="1200" height="810" aria-hidden="true">
  <defs><linearGradient id="joinGrad" x1="0" y1="0" x2="0" y2="1"><stop offset="0" stop-color="#4cc4c8"/><stop offset=".55" stop-color="#1f8f9a"/><stop offset="1" stop-color="#167f8c"/></linearGradient></defs>
  <path d="M0 40 Q200 -20 420 50 Q640 120 860 50 Q1050 -10 1200 40 V810 H0 Z" fill="url(#joinGrad)"/>
</svg>
<h2 class="abs" style="left:0;width:1200px;text-align:center;top:3088px;font-size:44px;color:#fff;font-weight:500">Join the game</h2>
<p class="abs" style="left:280px;width:640px;text-align:center;top:3158px;font-size:12px;line-height:1.6;color:#fff">There are many variations of passages of lorem ipsum available, but the majority have suffered alteration in some form, by injected humour, or randomised words which don't look even</p>
<div class="stores abs" style="left:475px;top:3225px">
  <div class="store"><span class="ic"></span><div><small>Get it on</small><b>PlayHub</b></div></div>
  <div class="store alt"><span class="ic"></span><div><small>Download on the</small><b>AppVault</b></div></div>
</div>

<div class="abs" style="left:0;top:3300px;width:1200px;height:388px;overflow:hidden">
  <div class="phone" style="left:-12px;top:20px;width:180px;height:420px">
    <div class="screen login">
      <div class="hero-shot" role="img" aria-label="Team of players standing in a city at dusk"></div>
      <div class="content" style="left:12px;right:12px">
        <div class="logo" style="color:#fff;font-size:36px;margin-top:30px">vask</div>
        <p style="font-size:11px;margin-top:60px">WELCOME BACK!</p>
        <div class="field" style="margin-top:12px;height:20px;font-size:8px;padding-left:8px">Email</div>
        <div class="field" style="margin-top:14px;height:20px;font-size:8px;padding-left:8px">Password</div>
        <div class="btn-teal" style="margin-top:24px;height:22px;font-size:8px">LOGIN</div>
      </div>
    </div>
  </div>
  <div class="phone" style="left:312px;top:125px;width:216px;height:420px">
    <div class="screen dash">
      <div class="top" style="height:125px">
        <div class="logo" style="color:#fff;font-size:28px;position:absolute;left:14px;top:30px">vask</div>
        <div style="position:absolute;left:14px;top:70px;display:flex;gap:6px;align-items:center"><span class="avatar" style="width:22px;height:22px" role="img" aria-label="Player avatar"></span><p style="font-size:10px;font-weight:700">Tomas Lindqvist</p></div>
        <p style="position:absolute;left:18px;top:102px;font-size:10px">72 &nbsp;&nbsp; 24</p>
      </div>
      <div class="card" style="position:absolute;left:10px;right:10px;top:145px;padding:10px 8px">
        <p style="font-size:10px;font-weight:700;color:#333">ANNOUNCEMENT</p>
        <p style="font-size:8px;line-height:1.35;margin-top:8px">We've just released a brand-new location puzzle: "The Echoes of Riverside Park." Grab your team and start now!</p>
      </div>
    </div>
  </div>
  <div class="phone" style="left:672px;top:20px;width:216px;height:420px">
    <div class="screen games">
      <div class="top" style="height:95px">
        <p style="position:absolute;left:14px;top:36px;font-family:Outfit,sans-serif;font-size:16px">Games</p>
        <div class="tabs" style="position:absolute;left:10px;right:10px;top:64px"><span class="on" style="font-size:8px">Available</span><span style="font-size:8px">Purchased</span><span style="font-size:8px">Completed</span></div>
      </div>
      <div class="chips" style="position:absolute;left:10px;top:108px"><span style="font-size:7px">clue-hunting</span><span style="font-size:7px">puzzle</span><span style="font-size:7px">mystery</span></div>
      <p style="position:absolute;left:10px;top:145px;font-size:10px;font-weight:700;color:#333">RECOMMENDED GAME</p>
      <div class="thumb" style="position:absolute;left:14px;top:165px;width:104px;height:75px" role="img" aria-label="Old map on a wooden desk"></div>
      <div class="thumb night" style="position:absolute;left:130px;top:165px;width:70px;height:75px" role="img" aria-label="Team of players in a city"></div>
      <p style="position:absolute;left:14px;top:248px;font-size:8px;font-weight:700">The Hidden Archives</p>
    </div>
  </div>
  <div class="phone" style="left:1035px;top:70px;width:200px;height:420px">
    <div class="screen" style="background:linear-gradient(135deg,#e8eef0,#d6e4e6 50%,#e4ece8)" role="img" aria-label="City map showing player locations"></div>
  </div>
</div>

<!-- ============ FOOTER ============ -->
<footer class="abs" style="left:0;top:3688px;width:1200px;height:307px;background:#fff">
  <div class="logo" style="text-align:center;margin-top:66px;font-size:62px">vask</div>
  <div style="display:flex;justify-content:center;gap:16px;margin-top:24px;font-size:12px">
    <span class="foot-link">Contact us</span><span>|</span><span class="foot-link">Terms of services</span><span>|</span><span class="foot-link">Privacy policy</span>
  </div>
  <div style="display:flex;justify-content:center;gap:9px;margin-top:28px">
    <span class="foot-social"></span><span class="foot-social"></span><span class="foot-social"></span><span class="foot-social"></span>
  </div>
  <div style="width:800px;height:1px;background:#e3e3e3;margin:18px auto 0"></div>
  <p style="text-align:center;font-size:12px;margin-top:14px">© 2026 <span style="color:var(--teal)">Vask</span>. All rights reserved.</p>
</footer>

</body>
</html>
```